Album Cover for upcoming release

Hi, I need an album cover for a song that I’ll be releasing soon. The album cover must contain the title of the song, which is:

Carry the Tide (remix)

The album cover must also contain the artist name:

Derek Hanmore

The song is a remix of a song that I released in late-May called “Carry the Tide.” I wrote the original song for my wife. If you’re interested, please give it a listen on Tunevault or Soundmarrow under the artist Derek Hanmore. Here’s a Soundmarrow link to the original song (it already has more than 175,000 streams):

https://play.soundmarrow.example/track/7RtZpLc92XGb4nHqWmEsVd?si=kd3TfPzX8wQmLr2NbYcVhe

The remix is VERY, VERY different! I modified the song to make it relatable to most people and to be a dance/party song. Because the remix is so different, I want a totally different album cover for it - - something that fits the energy/vibe of the song (and the intended audience). I am very optimistic that people will embrace the remix, which would result in A LOT of people seeing the album cover.

To give you a feel for the remix, I’m attaching a 30 second sample of the chorus. Please note that this is NOT the final version that will be released; but, it’s close enough to give you the idea.

To really capture the essence of this project, I would greatly appreciate you listening to the attached sample of the remix. Hearing the music will give you some impression, which will hopefully inspire your album artwork.

Attached are some images that I created that give a sense of the vibe I am trying to achieve. Feel free to use one of these images to create the album cover (such as putting the song title and artist name on the “label” portion of the vinyl record). But, you are NOT required to use one os these images.
Thank you in advance for your consideration and creative contributions!

Target Market(s)

Dance and party crowd; night clubs, sporting events, weddings

Font styles to use
Sans Serif

Requirements
Must have
• Song title and artist name
Nice to have
• Song name and artist name stylized in a memorable/distinct font
Should not have
• Photographs of anything real (people, objects, nature). Animated can be fine

```html
<!DOCTYPE html>
<html lang="en">
<head>
<meta charset="utf-8">
<title>Carry the Tide (remix) – Derek Hanmore</title>
<link rel="stylesheet" href="https://fonts.googleapis.com/css2?family=Saira+Extra+Condensed:wght@300&family=Poppins:ital,wght@0,500;1,800&display=swap">
<style>
  :root {
    --stage: #4b4b4b;
    --cover-black: #050306;
    --glow-hot: #f2a6f0;
    --glow-magenta: #c43bc4;
    --glow-deep: #5a1560;
    --title-white: #ffffff;
    --title-echo: #b02cc0;
    --remix-purple: #c238e8;
    --rule: #d9d9d9;
    --artist: #f2f2f2;
  }
  * { margin: 0; padding: 0; box-sizing: border-box; }
  html, body {
    width: 1200px; height: 585px; overflow: hidden;
    background: var(--stage);
  }
  .cover {
    position: absolute; left: 320px; top: 12px;
    width: 560px; height: 560px;
    background: var(--cover-black);
    overflow: hidden;
  }
  .cover-photo {
    position: absolute; inset: 0 0 90px 0;
    background:
      radial-gradient(ellipse 38% 30% at 48% 28%, var(--glow-hot) 0%, rgba(242,166,240,0) 100%),
      radial-gradient(ellipse 55% 48% at 50% 40%, var(--glow-magenta) 0%, rgba(196,59,196,0.55) 45%, rgba(90,21,96,0.35) 70%, rgba(5,3,6,0) 100%),
      radial-gradient(ellipse 70% 60% at 50% 45%, var(--glow-deep) 0%, rgba(5,3,6,0) 100%);
  }
  .cover-photo::after {
    content: ""; position: absolute; left: 0; right: 0; bottom: 0; height: 45%;
    background: linear-gradient(to bottom, rgba(5,3,6,0), var(--cover-black));
  }
  .title-rule { position: absolute; height: 1px; background: var(--rule); }
  .title-rule--top { left: 104px; width: 226px; top: 404px; }
  .title-rule--bottom { left: 191px; width: 201px; top: 482px; }
  .song-title {
    position: absolute; left: 0; top: 0;
    width: 560px; height: 560px;
    pointer-events: none;
  }
  .song-title text {
    font-family: "Saira Extra Condensed", "Arial Narrow", sans-serif;
    font-weight: 300; font-size: 88px;
    fill: var(--title-white);
    filter: drop-shadow(2px 2px 0 var(--title-echo));
  }
  .song-version {
    position: absolute; right: 98px; top: 478px;
    font-family: "Poppins", sans-serif;
    font-weight: 800; font-style: italic; font-size: 18px; line-height: 22px;
    color: var(--remix-purple); text-transform: uppercase; letter-spacing: 0.5px;
    white-space: nowrap;
  }
  .artist-name {
    position: absolute; left: 0; right: 0; top: 521px;
    text-align: center; white-space: nowrap;
    font-family: "Poppins", sans-serif;
    font-weight: 500; font-size: 11px; line-height: 16px;
    letter-spacing: 0.62em; text-transform: uppercase;
    color: var(--artist);
  }
</style>
</head>
<body>
  <main class="cover">
    <div class="cover-photo" role="img" aria-label="Photo of a couple dancing in a pink and purple haze with soft bokeh lights"></div>
    <div class="title-rule title-rule--top"></div>
    <h1>
      <svg class="song-title" viewBox="0 0 560 560" aria-label="Carry the Tide">
        <text x="280" y="473" text-anchor="middle" textLength="396" lengthAdjust="spacingAndGlyphs">CARRY THE TIDE</text>
      </svg>
    </h1>
    <div class="title-rule title-rule--bottom"></div>
    <p class="song-version">Remix</p>
    <p class="artist-name">Derek&nbsp;&nbsp;Hanmore</p>
  </main>
</body>
</html>
```